International Fundraising Consultancy needs a new PowerPoint Design

We train international nonprofits on how to fundraise globally. We plan to keep our current logo design and color, as we love the color orange, but want a cleaner, fresher, less cluttered template for our PowerPoint presentations. The finished product needs to be easy to edit, and include template slides that can feature tables, graphics and images. We would like a color scheme for graphics.The layout should be lighter, clear, attractive and easy to read and understand. We also want to use the same template for webinar slides. We have attached an example of our current PowerPoint template with identifying client information removed. The green slide that looks like a clapperboard fro a film is basically just a placeholder that indicates a break for an interactive exercise.

Target Market(s)

Board members, staff members, museum executives, leadership of NGOs, top businesspeople in Europe, many with a modern sense of aesthetics in the art world

Industry/Entity Type

Cleaner

Font styles to use
Sans Serif

Colors
f78f20
f37022

Requirements
Must have
• Orange colors, keep our Vormelinck logo
• Good templates for tables, photos and graphics

```html
<!DOCTYPE html>
<html lang="en">
<head>
<meta charset="utf-8">
<title>Project Title Slide</title>
<link rel="stylesheet" href="https://fonts.googleapis.com/css2?family=Roboto+Condensed:wght@400;700;900&display=swap">
<style>
  :root {
    --header-grey: #434343;
    --heading-orange: #f7a05e;
    --brand-orange: #f58a2a;
    --body-grey: #6e6e6e;
    --white: #ffffff;
  }
  * { margin: 0; padding: 0; box-sizing: border-box; }
  html, body { width: 1200px; height: 900px; overflow: hidden; background: var(--white); }
  .slide {
    position: relative;
    width: 1200px;
    height: 900px;
    background: var(--white);
    font-family: "Roboto Condensed", "Arial Narrow", sans-serif;
    overflow: hidden;
  }
  .slide-header {
    position: absolute;
    left: 0; top: 0;
    width: 1200px; height: 112px;
    background: var(--header-grey);
  }
  .slide-title {
    position: absolute;
    left: 28px; top: 26px;
    font-weight: 900;
    font-size: 47px;
    line-height: 58px;
    color: var(--white);
    letter-spacing: 0.3px;
  }
  .brand-name {
    position: absolute;
    right: 28px; top: 40px;
    font-weight: 400;
    font-size: 26px;
    line-height: 32px;
    color: var(--white);
  }
  .content-block {
    position: absolute;
    width: 500px;
  }
  .block-heading {
    font-weight: 700;
    font-size: 27px;
    line-height: 32px;
    color: var(--heading-orange);
    margin-bottom: 5px;
  }
  .block-text {
    font-weight: 400;
    font-size: 23.5px;
    line-height: 39px;
    color: var(--body-grey);
  }
  .block-top-left { left: 66px; top: 193px; }
  .block-top-right { left: 652px; top: 193px; }
  .block-bottom-left { left: 66px; top: 464px; }
  .block-bottom-right { left: 652px; top: 464px; }
  .slide-footer {
    position: absolute;
    left: 0; bottom: 0;
    width: 1200px; height: 33px;
    background: var(--brand-orange);
  }
</style>
</head>
<body>
<div class="slide">
  <header class="slide-header">
    <h1 class="slide-title">PROJECT TITLE HERE</h1>
    <span class="brand-name">Vormelinck</span>
  </header>

  <section class="content-block block-top-left">
    <h2 class="block-heading">SUBTEXT HERE SUBTEXT HERE</h2>
    <p class="block-text">Subtext here Subtext here Subtext here Subtext<br>here&nbsp; Subtext here Subtext here&nbsp; Subtext here<br>Subtext here&nbsp; Subtext here Subtext here Subtext<br>here Subtext here&nbsp; Subtext here Subtext here</p>
  </section>

  <section class="content-block block-top-right">
    <h2 class="block-heading">SUBTEXT HERE SUBTEXT HERE</h2>
    <p class="block-text">Subtext here Subtext here Subtext here Subtext<br>here&nbsp; Subtext here Subtext here&nbsp; Subtext here<br>Subtext here&nbsp; Subtext here Subtext here Subtext<br>here Subtext here&nbsp; Subtext here Subtext here</p>
  </section>

  <section class="content-block block-bottom-left">
    <h2 class="block-heading">SUBTEXT HERE SUBTEXT HERE</h2>
    <p class="block-text">Subtext here Subtext here Subtext here Subtext<br>here&nbsp; Subtext here Subtext here&nbsp; Subtext here<br>Subtext here&nbsp; Subtext here Subtext here Subtext<br>here Subtext here&nbsp; Subtext here Subtext here</p>
  </section>

  <section class="content-block block-bottom-right">
    <h2 class="block-heading">SUBTEXT HERE SUBTEXT HERE</h2>
    <p class="block-text">Subtext here Subtext here Subtext here Subtext<br>here&nbsp; Subtext here Subtext here&nbsp; Subtext here<br>Subtext here&nbsp; Subtext here Subtext here Subtext<br>here Subtext here&nbsp; Subtext here Subtext here</p>
  </section>

  <footer class="slide-footer"></footer>
</div>
</body>
</html>
```